Tolvek Marketing Consulting business card

I have a new logo that was designed for me here on PixelHarbor. I am a medical device marketing consultant. The medical device industry is very professional, kind of dry, and can be a bit boring. But I'm in marketing so I want to look fresh and innovative, within the confines of the industry.

Please use the logo to its potential, making it colorful and visually interesting (I know, there's really only one color. I need some kind of interesting design element - maybe wraparound...

Target Market(s)

Marketing management in medical device companies.

Industry/Entity Type

Marketing

Requirements
Must have
• Marisol Tolvek
Phone: 949-218-4073
Address: Harbor Crest, CA
marisol@tolvekmarketingconsulting.example
www.tolvekmarketingconsulting.example

```html
<!DOCTYPE html>
<html lang="en">
<head>
<meta charset="utf-8">
<title>Tolvek Marketing Consulting – Business Card</title>
<link rel="stylesheet" href="https://fonts.googleapis.com/css2?family=Open+Sans:wght@400;600;700&display=swap">
<style>
  :root {
    --backdrop: #2b2c2e;
    --card-white: #f7f8f9;
    --panel-grey: #4a4c4f;
    --panel-dark: #34363a;
    --brand-blue: #1d9ad6;
    --text-dark: #2a2b2d;
    --text-light: #ffffff;
  }
  * { box-sizing: border-box; margin: 0; padding: 0; }
  html, body { width: 1200px; height: 875px; overflow: hidden; }
  body {
    background: var(--backdrop);
    font-family: "Open Sans", Arial, sans-serif;
    position: relative;
  }
  .card {
    position: absolute;
    left: 320px;
    width: 560px;
    height: 320px;
    border-radius: 4px;
    overflow: hidden;
    background: var(--card-white);
    box-shadow: 0 10px 30px rgba(0,0,0,.45);
  }
  .card--back { top: 95px; }
  .card--front { top: 460px; }
  .card__art { position: absolute; inset: 0; }

  .back__content {
    position: absolute;
    right: 34px;
    top: 118px;
    text-align: right;
    color: var(--text-light);
  }
  .back__url { font-size: 13px; font-weight: 600; letter-spacing: .2px; margin-bottom: 6px; }
  .wordmark {
    display: flex;
    align-items: center;
    gap: 8px;
    font-weight: 600;
    white-space: nowrap;
  }
  .wordmark__mark { width: 14px; height: 14px; background: var(--brand-blue); flex: none; }
  .back__content .wordmark { justify-content: flex-end; font-size: 19px; color: var(--text-light); }

  .front__identity { position: absolute; left: 34px; top: 40px; }
  .front__name { font-size: 24px; font-weight: 400; color: var(--brand-blue); line-height: 1.1; }
  .front__title { font-size: 14px; color: var(--text-dark); margin-top: 2px; }

  .front__contact {
    position: absolute;
    right: 150px;
    top: 92px;
    text-align: right;
    font-size: 12.5px;
    color: var(--text-dark);
    line-height: 1.9;
    white-space: nowrap;
  }
  .contact-line { display: flex; align-items: center; justify-content: flex-end; gap: 8px; }
  .contact-line svg { flex: none; }

  .front__brand {
    position: absolute;
    left: 34px;
    bottom: 38px;
    color: var(--text-dark);
    white-space: nowrap;
  }
  .front__email { font-size: 13px; margin-bottom: 16px; }
  .front__url { font-size: 11px; font-weight: 600; margin-bottom: 2px; }
  .front__brand .wordmark { font-size: 18px; color: var(--brand-blue); }
  .front__location { font-size: 13px; color: var(--brand-blue); margin-top: 4px; padding-left: 22px; }
</style>
</head>
<body>

<section class="card card--back" aria-label="Card back">
  <svg class="card__art" viewBox="0 0 560 320" aria-hidden="true">
    <rect x="0" y="0" width="560" height="320" fill="var(--card-white)"/>
    <polygon points="210,0 560,0 560,320 150,320" fill="var(--panel-grey)"/>
    <polygon points="188,0 206,0 146,320 128,320" fill="var(--brand-blue)"/>
    <polygon points="0,220 20,220 20,320 0,320" fill="var(--brand-blue)"/>
  </svg>
  <div class="back__content">
    <p class="back__url">www.tolvekmarketingconsulting.example</p>
    <p class="wordmark"><span class="wordmark__mark"></span>Tolvek Marketing Consulting</p>
  </div>
</section>

<section class="card card--front" aria-label="Card front">
  <svg class="card__art" viewBox="0 0 560 320" aria-hidden="true">
    <rect x="0" y="0" width="560" height="320" fill="var(--card-white)"/>
    <polygon points="470,0 560,0 560,320 440,320" fill="var(--panel-dark)"/>
    <rect x="420" y="0" width="22" height="320" fill="var(--brand-blue)"/>
  </svg>

  <div class="front__identity">
    <h1 class="front__name">Marisol Tolvek</h1>
    <p class="front__title">Managing Director</p>
  </div>

  <div class="front__contact">
    <p class="contact-line">949-218-4073
      <svg width="16" height="16" viewBox="0 0 16 16" aria-label="Phone"><circle cx="8" cy="8" r="7.5" fill="none" stroke="var(--brand-blue)"/><path d="M5 4.5l1.5-.5 1 2-1 .8a5 5 0 0 0 2.2 2.2l.8-1 2 1-.5 1.5c-3.5 0-6-2.5-6-6z" fill="var(--brand-blue)"/></svg>
    </p>
    <p class="contact-line">www.tolvekmarketingconsulting.example
      <svg width="16" height="16" viewBox="0 0 16 16" aria-label="Web"><circle cx="8" cy="8" r="7.5" fill="none" stroke="var(--brand-blue)"/><circle cx="8" cy="8" r="4" fill="none" stroke="var(--brand-blue)"/><path d="M4 8h8M8 4v8" stroke="var(--brand-blue)"/></svg>
    </p>
  </div>

  <div class="front__brand">
    <p class="front__email">marisol@tolvekmarketingconsulting.example</p>
    <p class="front__url">www.tolvekmarketingconsulting.example</p>
    <p class="wordmark"><span class="wordmark__mark"></span>Tolvek Marketing Consulting</p>
    <p class="front__location">Harbor Crest, CA</p>
  </div>
</section>

</body>
</html>
```